E-Commerce Custom Design Magento Standard Requirements For Marketing Agency

I need to revamp theme for a website www.ironvaleoutreach.com and want to change name to www.ironvalebrokers.com I have logo attached. I need a custom e commerce website built that pops and grabs attention. My logo is silver and looks great on black background. Please just use all same content from existing website www.ironvaleoutreach.com and use existing products that you see there.

Target Market(s)

REAL ESTATE AGENTS

Industry/Entity Type

Digital Marketing

Coding

Coded - Design and coding required

Number of Pages Required

5+ page

Colors

Designer to choose colors to be used in the design.

Requirements
Must have
• Please revamp entire website www.ironvaleoutreach.com and use new logo attached. Domain name will be www.ironvalebrokers.com and will offer marketing services for real estate agents around the country and world. Specializing in digital marketing services such as Lumora Ads, Pixavel Ads, Vell Rion Ads, Quorvia Bidlane, Etc.
Nice to have
Should not have

```html
<!DOCTYPE html>
<html lang="en">
<head>
<meta charset="utf-8">
<title>Ironvale Brokers — Digital Marketing for Realtors</title>
<link href="https://fonts.googleapis.com/css2?family=Montserrat:wght@300;400;500;600;700&display=swap" rel="stylesheet">
<style>
:root{
  --ink:#1c1c1c;
  --muted:#6d6d6d;
  --line:#e4e4e4;
  --gold:#b8860b;
  --gold-btn:#a8790c;
  --btn-grey:#e2e2e2;
  --footer:#2b2b2b;
  --footer-text:#c9c9c9;
  --white:#ffffff;
}
*{margin:0;padding:0;box-sizing:border-box}
html,body{width:1200px;height:3805px;overflow:hidden}
body{font-family:'Montserrat',sans-serif;color:var(--ink);background:var(--white);position:relative}

.hero{position:absolute;left:0;top:0;width:1200px;height:609px;
  background:linear-gradient(180deg,#1d2330 0%,#2b3444 35%,#3a3f48 60%,#1a1b1f 100%)}
.site-nav{position:absolute;left:0;top:0;width:1200px;height:84px}
.brand{position:absolute;left:22px;top:26px;display:flex;align-items:center;gap:8px;color:#d9d9d9;font-weight:700;font-size:15px;letter-spacing:1px}
.brand-mark{width:18px;height:18px;border-radius:50%;background:#cfcfcf}
.nav-links{position:absolute;top:33px;left:776px;display:flex;gap:30px;font-size:11px;color:var(--white);font-weight:500}
.nav-cart{position:absolute;left:966px;top:31px}
.nav-contact{position:absolute;left:1012px;top:26px;width:94px;height:28px;border:1.5px solid var(--white);border-radius:14px;color:var(--white);font-size:10px;font-weight:700;text-align:center;line-height:25px;letter-spacing:.5px}
.hero-kicker{position:absolute;top:234px;width:100%;text-align:center;color:var(--white);font-weight:400;font-size:26px}
.hero-title{position:absolute;top:272px;width:100%;text-align:center;color:var(--white);font-weight:700;font-size:40px}
.hero-btn{position:absolute;left:533px;top:344px;width:140px;height:38px;border-radius:19px;background:var(--gold-btn);color:var(--white);font-size:10px;font-weight:700;display:flex;align-items:center;justify-content:center;gap:10px}

.advantages{position:absolute;top:690px;left:90px;width:1020px;display:flex;gap:20px}
.advantage{flex:1;display:flex;gap:14px}
.advantage svg{flex:none}
.advantage h3{font-size:13px;font-weight:500;margin-bottom:8px}
.advantage p{font-size:10px;line-height:1.6;color:var(--muted)}
.rule{position:absolute;top:850px;left:0;width:1200px;height:1px;background:var(--line)}

.section-title{position:absolute;top:932px;left:92px;font-size:27px;font-weight:600}
.products{position:absolute;top:1010px;left:94px;width:1012px;display:grid;grid-template-columns:repeat(3,325px);column-gap:18px;grid-auto-rows:481px}
.product{position:relative}
.product-media{width:325px;height:213px}
.product-name{margin-top:28px;font-size:13px;font-weight:600;line-height:1.5}
.product-desc{margin-top:12px;font-size:9.5px;line-height:1.7;color:var(--muted)}
.product-foot{position:absolute;top:354px;left:0;width:325px;border-top:1px solid var(--line);padding-top:12px;display:flex;align-items:center;gap:22px}
.price-old{display:block;font-size:9px;color:#999;text-decoration:line-through}
.price-new{display:block;font-size:12px;font-weight:500;color:var(--gold)}
.add-cart{width:88px;height:28px;background:var(--btn-grey);font-size:8.5px;font-weight:600;display:flex;align-items:center;justify-content:center}

.site-footer{position:absolute;top:3471px;left:0;width:1200px;height:334px;background:var(--footer);color:var(--footer-text)}
.footer-brand{position:absolute;left:125px;top:86px;display:flex;align-items:center;gap:8px;color:#e0e0e0;font-weight:700;font-size:15px;letter-spacing:1px}
.footer-heading{position:absolute;left:490px;top:66px;font-size:11px;font-weight:700;color:var(--white)}
.footer-list{position:absolute;top:106px;list-style:none;font-size:9.5px;line-height:25px}
.social{position:absolute;left:93px;top:254px;display:flex;gap:18px}
.social span{width:12px;height:12px;border-radius:50%;background:#777}
</style>
</head>
<body>
<header class="hero" role="img" aria-label="Photograph of a modern luxury home at dusk with lit stone steps">
  <nav class="site-nav">
    <div class="brand"><span class="brand-mark"></span>IRONVALE</div>
    <div class="nav-links"><span>Products</span><span>About</span><span>Login</span></div>
    <svg class="nav-cart" width="16" height="14" viewBox="0 0 16 14"><path d="M1 1h3l2 8h8l1.5-6H5" fill="none" stroke="#fff" stroke-width="1.4"/><circle cx="7" cy="12" r="1.2" fill="#fff"/><circle cx="13" cy="12" r="1.2" fill="#fff"/></svg>
    <div class="nav-contact">CONTACT</div>
  </nav>
  <p class="hero-kicker">Advanced Digital Marketing Services</p>
  <h1 class="hero-title">For The „No So Average“ Realtor</h1>
  <div class="hero-btn">VIEW SERVICES <svg width="12" height="8" viewBox="0 0 12 8"><path d="M0 4h10M7 1l3 3-3 3" fill="none" stroke="#fff" stroke-width="1.3"/></svg></div>
</header>

<section class="advantages">
  <div class="advantage">
    <svg width="30" height="30" viewBox="0 0 30 30"><path d="M4 14L15 5l11 9M7 12v13h16V12M12 25v-7h6v7" fill="none" stroke="#b8860b" stroke-width="1.5"/></svg>
    <div><h3>Your advantage 01</h3><p>Lorem ipsum dolor sit amet, consectetur adipiscing elit, sed do eiusmod tempor incididunt ut labore</p></div>
  </div>
  <div class="advantage">
    <svg width="30" height="30" viewBox="0 0 30 30"><path d="M4 6h22v14H12l-6 5v-5H4z" fill="none" stroke="#b8860b" stroke-width="1.5"/><path d="M10 13h10" stroke="#b8860b" stroke-width="1.5"/></svg>
    <div><h3>Your advantage 02</h3><p>Lorem ipsum dolor sit amet, consectetur adipiscing elit, sed do eiusmod tempor incididunt ut labore</p></div>
  </div>
  <div class="advantage">
    <svg width="30" height="30" viewBox="0 0 30 30"><path d="M15 4v22M6 9h18M6 9l-3 8h6zM24 9l-3 8h6zM10 26h10" fill="none" stroke="#b8860b" stroke-width="1.5"/></svg>
    <div><h3>Your advantage 03</h3><p>Lorem ipsum dolor sit amet, consectetur adipiscing elit, sed do eiusmod tempor incididunt ut labore</p></div>
  </div>
  <div class="advantage">
    <svg width="30" height="30" viewBox="0 0 30 30"><path d="M5 26V12l10-7 10 7v14zM11 26v-8h8v8" fill="none" stroke="#b8860b" stroke-width="1.5"/></svg>
    <div><h3>Your advantage 04</h3><p>Lorem ipsum dolor sit amet, consectetur adipiscing elit, sed do eiusmod tempor incididunt ut labore</p></div>
  </div>
</section>
<div class="rule"></div>

<h2 class="section-title">Our Services</h2>
<main class="products">
  <article class="product">
    <div class="product-media" role="img" aria-label="Sketch of social media network doodles on paper" style="background:linear-gradient(135deg,#f1f1ef,#cfd6dc)"></div>
    <h3 class="product-name">Ironvale Social Growth Engine</h3>
    <p class="product-desc">We will create new, fresh relevant social media content for your business and post it daily to your Pixavel and Lumora business pages FOR YOU. We also Guarantee to add hundreds of new followers (not ghost followers) to your Pixavel page every month.</p>
    <div class="product-foot"><div><span class="price-old">$349.00</span><span class="price-new">$249.00</span></div><div class="add-cart">ADD TO CART</div></div>
  </article>
  <article class="product">
    <div class="product-media" role="img" aria-label="Photo of social ads text on a screen" style="background:linear-gradient(135deg,#1e2a44,#44557a)"></div>
    <h3 class="product-name">Lumora Ad For One Open Hous</h3>
    <p class="product-desc">We will run an Lumora Ad targeted to all residents in the neighborhood and surrounding neighborhood of your open house</p>
    <div class="product-foot"><div><span class="price-old">$349.00</span><span class="price-new">$249.00</span></div><div class="add-cart">ADD TO CART</div></div>
  </article>
  <article class="product">
    <div class="product-media" role="img" aria-label="Photo of a desk phone with a voice mail key" style="background:linear-gradient(135deg,#3a3a3a,#8a8a8a)"></div>
    <h3 class="product-name">Voice Broadcast Marketing For One Open House</h3>
    <p class="product-desc">Leave up to 300 voicemails to residents in the neighborhood and surrounding neighborhood of your open house informing them of your open house</p>
    <div class="product-foot"><div><span class="price-old">$349.00</span><span class="price-new">$249.00</span></div><div class="add-cart">ADD TO CART</div></div>
  </article>

  <article class="product">
    <div class="product-media" role="img" aria-label="Illustration of blue puzzle pieces about SMS advertising" style="background:linear-gradient(135deg,#eef1f4,#9fb8d4)"></div>
    <h3 class="product-name">SMS Marketing For One Open House</h3>
    <p class="product-desc">Send up to 300 text messages to residents in the neighborhood and surrounding neighborhood of your open house informing them of your open house</p>
    <div class="product-foot"><div><span class="price-old">$349.00</span><span class="price-new">$249.00</span></div><div class="add-cart">ADD TO CART</div></div>
  </article>
  <article class="product">
    <div class="product-media" role="img" aria-label="Photo of app icons on a phone screen" style="background:linear-gradient(135deg,#2c3a66,#8a6fa8)"></div>
    <h3 class="product-name">Pixavel Ad For One Open House</h3>
    <p class="product-desc">We will run an Pixavel Ad targeted to all residents in the neighborhood and surrounding neighborhood of your open house</p>
    <div class="product-foot"><div><span class="price-old">$349.00</span><span class="price-new">$249.00</span></div><div class="add-cart">ADD TO CART</div></div>
  </article>
  <article class="product">
    <div class="product-media" role="img" aria-label="Graphic of two social app tiles side by side" style="background:#eef0f2"></div>
    <h3 class="product-name">Lumora &amp; Pixavel Ad Combo For One Open House</h3>
    <p class="product-desc">We will run a Lumora and Pixavel ad targeted to all residents in the neighborhood and surrounding neighborhood of your open house</p>
    <div class="product-foot"><div><span class="price-old">$349.00</span><span class="price-new">$249.00</span></div><div class="add-cart">ADD TO CART</div></div>
  </article>

  <article class="product">
    <div class="product-media" role="img" aria-label="Illuminated e-mail marketing sign" style="background:linear-gradient(135deg,#14205a,#3b56b8)"></div>
    <h3 class="product-name">Email Marketing For One Open House</h3>
    <p class="product-desc">Send up to 300 text messages to residents in the neighborhood and surrounding neighborhood of your open house informing them of your open house</p>
    <div class="product-foot"><div><span class="price-old">$349.00</span><span class="price-new">$249.00</span></div><div class="add-cart">ADD TO CART</div></div>
  </article>
  <article class="product">
    <div class="product-media" role="img" aria-label="Placeholder product image" style="background:#f3f3f3"></div>
    <h3 class="product-name">Email &amp; SMS &amp; VB Marketing Combo For One Open House</h3>
    <p class="product-desc">Send up to 1500 text messages, voicemails and emails (up to 500 of each) to residents in the neighborhood and surrounding neighborhood of your open house</p>
    <div class="product-foot"><div><span class="price-old">$349.00</span><span class="price-new">$249.00</span></div><div class="add-cart">ADD TO CART</div></div>
  </article>
  <article class="product">
    <div class="product-media" role="img" aria-label="Illustration of a megaphone with marketing icons" style="background:linear-gradient(135deg,#f7f9fb,#cfe0f2)"></div>
    <h3 class="product-name">All Marketing Services For One Ipen House</h3>
    <p class="product-desc">Send up to 1500 text messages, voicemails and emails (up to 500 of each) to residents in the neighborhood and surrounding neighborhood of your open house</p>
    <div class="product-foot"><div><span class="price-old">$349.00</span><span class="price-new">$249.00</span></div><div class="add-cart">ADD TO CART</div></div>
  </article>

  <article class="product">
    <div class="product-media" role="img" aria-label="Sketch of social media network doodles on paper" style="background:linear-gradient(135deg,#f1f1ef,#cfd6dc)"></div>
    <h3 class="product-name">All Ironvale Realtor Open House Marketing Services</h3>
    <p class="product-desc">Includes SMS, Voicemail Drops, Email Marketing, Lumora &amp; Pixavel Ads.</p>
    <div class="product-foot"><div><span class="price-old">$349.00</span><span class="price-new">$249.00</span></div><div class="add-cart">ADD TO CART</div></div>
  </article>
  <article class="product">
    <div class="product-media" role="img" aria-label="Photo of a hand holding a phone with a messenger app" style="background:linear-gradient(135deg,#6b5f52,#c9c2b8)"></div>
    <h3 class="product-name">Lumora Messenger Marketing Smart Social Connect</h3>
    <p class="product-desc">We Send Messages On Your Behalf Through Lumora Messenger To All Customers That Have Engaged (Liked, Commented, Shared) With Your Lumora Business Page or Posts (Paid &amp; Unpaid).</p>
    <div class="product-foot"><div><span class="price-old">$349.00</span><span class="price-new">$249.00</span></div><div class="add-cart">ADD TO CART</div></div>
  </article>
  <article class="product">
    <div class="product-media" role="img" aria-label="Chalk sketch of social media profile tools on wood" style="background:linear-gradient(135deg,#c9a673,#8f6b3d)"></div>
    <h3 class="product-name">Lumora and Pixavel Business Profiles Set Up</h3>
    <p class="product-desc">We Will Build A Lumora &amp; Pixavel Profile For Your Business and Deliver It In 3 days.</p>
    <div class="product-foot"><div><span class="price-old">$349.00</span><span class="price-new">$249.00</span></div><div class="add-cart">ADD TO CART</div></div>
  </article>

  <article class="product">
    <div class="product-media" role="img" aria-label="Screenshot of a social business page" style="background:linear-gradient(135deg,#e9edf3,#8fa0b8)"></div>
    <h3 class="product-name">Monthly Lumora Marketing Management Fully Scalable Agency</h3>
    <p class="product-desc">Optimized For Lead Generation, New Sales and Repeat Business With Full Reporting, Laser Targeting – Full Lumora Advertising Management</p>
    <div class="product-foot"><div><span class="price-old">$349.00</span><span class="price-new">$249.00</span></div><div class="add-cart">ADD TO CART</div></div>
  </article>
  <article class="product">
    <div class="product-media" role="img" aria-label="Chalkboard with the word remarketing" style="background:linear-gradient(135deg,#1f5a3c,#3c7a58)"></div>
    <h3 class="product-name">Lumora Remarketing Campaign</h3>
    <p class="product-desc">Remarket To Your Website Visitors and Your Current/Past Customers Right On Their Lumora Newsfeeds.</p>
    <div class="product-foot"><div><span class="price-old">$349.00</span><span class="price-new">$249.00</span></div><div class="add-cart">ADD TO CART</div></div>
  </article>
</main>

<footer class="site-footer">
  <div class="footer-brand"><span class="brand-mark"></span>IRONVALE</div>
  <h4 class="footer-heading">SERVICES</h4>
  <ul class="footer-list" style="left:490px">
    <li>Ironvale social growth engine</li>
    <li>Lumora ad for one open house</li>
    <li>Voice broadcast marketing for one open house</li>
    <li>SMS marketing for one open house</li>
    <li>Pixavel ad for one open house</li>
    <li>Lumora &amp; Pixavel ad combo for one open house</li>
    <li>Email marketing for one open house</li>
  </ul>
  <ul class="footer-list" style="left:802px">
    <li>Email &amp; SMS &amp; VB marketing combo for One open house</li>
    <li>All marketing services for one open house</li>
    <li>All ironvale realtor open house marketing services</li>
    <li>Lumora messenger marketing smart social connect</li>
    <li>Lumora and Pixavel business profiles set up</li>
    <li>Monthly Lumora marketing management</li>
    <li>Lumora remarketing campaign</li>
  </ul>
  <div class="social"><span></span><span></span><span></span></div>
</footer>
</body>
</html>
```